Business card

creative business card for newly created national firm that specializes in high-density storage for retail markets. Looking for creativity and overall theme that will differentiate from others in this unique niche ...essentially a design that will provide instant recognition as we develop our identity in the marketplace. possible initial thoughts are attached with logo separately

Retail

```html
<!DOCTYPE html>
<html lang="en">
<head>
<meta charset="utf-8">
<title>Stackwise Storage – Business Card</title>
<link rel="stylesheet" href="https://fonts.googleapis.com/css2?family=Lato:wght@400;700;900&display=swap">
<style>
  :root {
    --bg: #e9e6e1;
    --blue-light: #6ccbea;
    --blue-mid: #3fb0dc;
    --blue-deep: #2a97c6;
    --ink-dark: #1d5874;
    --ink-label: #174a63;
    --white: #ffffff;
    --card-white: #fbfbfb;
    --logo-teal: #2f8fb6;
    --shadow: rgba(40, 50, 60, 0.18);
  }
  * { margin: 0; padding: 0; box-sizing: border-box; }
  html, body {
    width: 759px;
    height: 1200px;
    overflow: hidden;
    background: var(--bg);
    font-family: "Lato", Arial, sans-serif;
  }
  .canvas {
    position: relative;
    width: 759px;
    height: 1200px;
  }
  .card {
    position: absolute;
    border-radius: 16px;
    box-shadow: 0 10px 28px var(--shadow);
  }

  /* Front: contact side */
  .card-front {
    left: 229px;
    top: 60px;
    width: 300px;
    height: 525px;
    background: linear-gradient(160deg, var(--blue-light) 0%, var(--blue-mid) 55%, var(--blue-deep) 100%);
    padding: 38px 30px 34px;
    text-align: right;
    color: var(--ink-dark);
  }
  .person-name {
    font-weight: 700;
    font-size: 22px;
    letter-spacing: 1px;
    color: var(--white);
    text-transform: uppercase;
  }
  .person-phone {
    font-weight: 700;
    font-size: 19px;
    letter-spacing: 0.5px;
    margin-top: 4px;
    color: var(--ink-dark);
  }
  .contact-block { margin-top: 36px; }
  .contact-label {
    font-weight: 700;
    font-size: 15px;
    color: var(--ink-label);
    text-decoration: underline;
    text-align: center;
    padding-left: 60px;
    margin-bottom: 6px;
  }
  .contact-line {
    font-size: 14px;
    line-height: 1.35;
    color: var(--white);
  }
  .contact-email { font-size: 12.5px; }
  .card-website {
    position: absolute;
    left: 30px;
    right: 30px;
    bottom: 34px;
    font-weight: 700;
    font-size: 14px;
    color: var(--ink-dark);
    text-align: left;
  }

  /* Back: brand side */
  .card-back {
    left: 80px;
    top: 700px;
    width: 600px;
    height: 343px;
    background: var(--card-white);
    display: flex;
    flex-direction: column;
    align-items: center;
    justify-content: center;
    padding: 0 40px;
  }
  .brand-row {
    display: flex;
    align-items: center;
    gap: 16px;
  }
  .brand-square {
    width: 32px;
    height: 32px;
    background: var(--logo-teal);
    flex: none;
  }
  .brand-name {
    font-weight: 400;
    font-size: 38px;
    letter-spacing: 3px;
    color: var(--logo-teal);
    text-transform: uppercase;
    white-space: nowrap;
  }
  .brand-tagline {
    margin-top: 18px;
    font-weight: 700;
    font-size: 16px;
    letter-spacing: 3px;
    color: var(--ink-dark);
  }
</style>
</head>
<body>
<main class="canvas">
  <section class="card card-front" aria-label="Business card front">
    <p class="person-name">Dana Whitfield</p>
    <p class="person-phone">855-RACK-ROOM</p>

    <div class="contact-block">
      <p class="contact-label">Office</p>
      <p class="contact-line">Juniper Avenue Address</p>
      <p class="contact-line">Millbrook, CO 80000</p>
    </div>

    <div class="contact-block">
      <p class="contact-label">E-Mail</p>
      <p class="contact-line contact-email">hello@stackwisestorage.com</p>
    </div>

    <div class="contact-block">
      <p class="contact-label">Mail</p>
      <p class="contact-line">PO Box 4470</p>
      <p class="contact-line">Millbrook, CO 80001</p>
    </div>

    <p class="card-website">www.stackwisestorage.com</p>
  </section>

  <section class="card card-back" aria-label="Business card back">
    <div class="brand-row">
      <span class="brand-square" aria-hidden="true"></span>
      <span class="brand-name">Stackwise Storage</span>
    </div>
    <p class="brand-tagline">Stack Smarter Daily</p>
  </section>
</main>
</body>
</html>
```